" Visitamos clientes importadores e vendemos nossos servicos. Eles nos fornecem a factura a qual desejam importar e nos tratamos de todo o processo de desalfandegamento da mercadoria ate o transporte e entrega no armazem dos nossos clientes. "

```html
<!DOCTYPE html>
<html lang="pt">
<head>
<meta charset="utf-8">
<title>Porto Vale – Envelope</title>
<link rel="stylesheet" href="https://fonts.googleapis.com/css2?family=Montserrat:wght@400;600;800&display=swap">
<style>
  :root {
    --navy: #1f2a8c;
    --navy-soft: #2a36a0;
    --paper: #ffffff;
    --ink: #2b2f45;
    --muted: #6b6f82;
    --mark-faint: rgba(255, 255, 255, 0.08);
    --mark-faint-dark: rgba(31, 42, 140, 0.06);
    --stage: #e9eaee;
  }
  * { box-sizing: border-box; margin: 0; padding: 0; }
  html, body {
    width: 1200px; height: 1200px; overflow: hidden;
    background: var(--stage);
    font-family: "Montserrat", sans-serif;
  }
  .canvas {
    width: 1200px; height: 1200px;
    display: flex; align-items: center; justify-content: center; gap: 60px;
  }
  .envelope {
    position: relative;
    width: 480px; height: 680px;
    overflow: hidden;
    box-shadow: 0 12px 30px rgba(0,0,0,0.12);
  }
  .envelope--front { background: var(--paper); }
  .envelope--back { background: var(--navy); }

  .flap-edge {
    position: absolute; top: 0; right: 0;
    width: 56px; height: 100%;
  }
  .bottom-band {
    position: absolute; left: 0; bottom: 0;
    width: 100%; height: 22px;
    background: var(--navy);
  }

  .brand { position: absolute; display: flex; align-items: center; gap: 12px; }
  .brand__dot { width: 34px; height: 34px; border-radius: 50%; }
  .brand__name {
    font-weight: 800; font-size: 30px; letter-spacing: 1px; line-height: 1;
  }
  .brand__tagline {
    font-size: 9px; font-weight: 400; letter-spacing: 0.5px; margin-top: 4px;
  }
  .envelope--front .brand { top: 60px; left: 40px; }
  .envelope--front .brand__dot { background: var(--navy); }
  .envelope--front .brand__name { color: var(--navy); }
  .envelope--front .brand__tagline { color: var(--muted); }

  .envelope--back .brand { bottom: 110px; left: 60px; }
  .envelope--back .brand__dot { background: #ffffff; }
  .envelope--back .brand__name { color: #ffffff; }
  .envelope--back .brand__tagline { color: rgba(255,255,255,0.75); }

  .mark-faint {
    position: absolute; border-radius: 50%;
    width: 260px; height: 260px;
  }
  .envelope--front .mark-faint { top: 170px; left: 80px; background: var(--mark-faint-dark); }
  .envelope--back .mark-faint { top: 200px; left: 150px; background: var(--mark-faint); }

  .contact {
    position: absolute; left: 40px; bottom: 50px;
    display: grid; grid-template-columns: auto auto; column-gap: 40px; row-gap: 6px;
    font-size: 11px; color: var(--ink);
  }
  .contact__item { display: flex; align-items: center; gap: 6px; }
  .contact__item svg { width: 11px; height: 11px; fill: var(--navy); }
</style>
</head>
<body>
<main class="canvas">

  <section class="envelope envelope--front" aria-label="Frente do envelope">
    <svg class="flap-edge" viewBox="0 0 56 680" preserveAspectRatio="none" aria-hidden="true">
      <polygon points="0,0 56,0 56,680 40,680 40,70" fill="var(--navy)"/>
    </svg>
    <div class="brand">
      <span class="brand__dot"></span>
      <div>
        <div class="brand__name">PORTO VALE</div>
        <div class="brand__tagline">Despacho aduaneiro e logística</div>
      </div>
    </div>
    <div class="mark-faint"></div>
    <div class="contact">
      <span class="contact__item">
        <svg viewBox="0 0 24 24"><path d="M6.6 10.8a15 15 0 0 0 6.6 6.6l2.2-2.2a1 1 0 0 1 1-.25 11 11 0 0 0 3.6.6 1 1 0 0 1 1 1V20a1 1 0 0 1-1 1A17 17 0 0 1 3 4a1 1 0 0 1 1-1h3.5a1 1 0 0 1 1 1 11 11 0 0 0 .6 3.6 1 1 0 0 1-.25 1z"/></svg>
        (00) 0000-0000
      </span>
      <span class="contact__item">
        <svg viewBox="0 0 24 24"><path d="M2 5h20v14H2z M2 5l10 7 10-7" fill="none" stroke="var(--navy)" stroke-width="2"/></svg>
        contato@portovale.com.br
      </span>
      <span class="contact__item">
        <svg viewBox="0 0 24 24"><circle cx="12" cy="12" r="10"/></svg>
        (00) 0000-0000
      </span>
      <span class="contact__item">
        <svg viewBox="0 0 24 24"><circle cx="12" cy="12" r="9" fill="none" stroke="var(--navy)" stroke-width="2"/><path d="M3 12h18M12 3c3 3 3 15 0 18M12 3c-3 3-3 15 0 18" fill="none" stroke="var(--navy)" stroke-width="1.5"/></svg>
        www.portovale.com.br
      </span>
    </div>
    <div class="bottom-band"></div>
  </section>

  <section class="envelope envelope--back" aria-label="Verso do envelope">
    <div class="mark-faint"></div>
    <div class="brand">
      <span class="brand__dot"></span>
      <div>
        <div class="brand__name">PORTO VALE</div>
        <div class="brand__tagline">Despacho aduaneiro e logística</div>
      </div>
    </div>
  </section>

</main>
</body>
</html>
```